"Cork Hollow Excursions" is a top notch Santa Barbara County Wine Tour company.

We provide scenic, boutique and custom wine tours. I need the card to be clean and classy. I will provide our logo. I would like the logo to cover the back side of the card as an option and would like to see a couple color options other then our signature green and gold. I would like to see some creative options and let the designers come up with options.
I need cards for myself and my team. The final design should communicate "An authentic and boutique wine tour experience"
Please use my website for reference www.corkhollowexcursions.com

Target Market(s)

We have a wide range of clients from millennials to baby boomers

Industry/Entity Type

Tour

Contact Information for Business Card

Contact info:
Dale Munford
805-291-6384
info@corkhollowexcursions.com
corkhollowexcursions.com

Colors

Designer to choose colors to be used in the design.

Requirements
Must have
• my logo
Nice to have
• *I would like to have the backside side with the logo and the company statement
• "An authentic and boutique wine tour experience" as an option.
• *I would also like to see what the designers can create!
• *I would like to see an option that incorporates or social: snapgrid, rovia, route scout
Should not have
• I do not want it too busy.

```html
<!DOCTYPE html>
<html lang="en">
<head>
<meta charset="utf-8">
<title>Cork Hollow Excursions – Business Card</title>
<link href="https://fonts.googleapis.com/css2?family=Open+Sans:wght@400;600;700&display=swap" rel="stylesheet">
<style>
  :root {
    --bg: #e9eae8;
    --card: #ffffff;
    --green: #23633f;
    --green-soft: #5d8f70;
    --ink: #2b2b2b;
    --rule: #b9cfc1;
    --gold: #9a7f5e;
  }
  * { box-sizing: border-box; margin: 0; padding: 0; }
  html, body {
    width: 1200px; height: 864px; overflow: hidden;
    background: var(--bg);
    font-family: "Open Sans", Arial, sans-serif;
  }
  .stage { position: relative; width: 1200px; height: 864px; }

  .card {
    position: absolute;
    width: 600px; height: 340px;
    background: var(--card);
    box-shadow: 0 6px 18px rgba(0,0,0,.12);
    overflow: hidden;
  }

  /* Back side */
  .card--back { left: 300px; top: 70px; }
  .back__scene {
    position: absolute; left: 0; top: 0; width: 600px; height: 258px;
    background: linear-gradient(180deg, #ffffff 0%, #ffffff 28%, #8fb59d 55%, var(--green) 100%);
  }
  .back__band {
    position: absolute; left: 0; bottom: 0; width: 600px; height: 82px;
    background: var(--green);
    border-top: 3px solid #ffffff;
    display: flex; align-items: center; justify-content: center;
  }
  .back__tagline {
    color: #ffffff; font-weight: 600; font-size: 19px; letter-spacing: .2px;
  }

  /* Front side */
  .card--front { left: 300px; top: 450px; }
  .front__brand {
    position: absolute; right: 40px; top: 70px;
    display: flex; align-items: center; gap: 10px;
  }
  .brand__mark { width: 14px; height: 14px; background: var(--green); }
  .brand__name {
    font-weight: 600; font-size: 26px; color: var(--gold); letter-spacing: .5px;
  }
  .front__name {
    position: absolute; left: 40px; top: 150px;
    font-weight: 700; font-size: 21px; color: var(--green);
  }
  .front__rule {
    position: absolute; left: 200px; right: 40px; top: 188px;
    height: 1px; background: var(--rule);
  }
  .front__contacts {
    position: absolute; right: 36px; top: 210px;
    list-style: none; text-align: right;
  }
  .contact {
    display: flex; justify-content: flex-end; align-items: center; gap: 10px;
    font-size: 16px; color: var(--ink); line-height: 26px;
  }
  .contact svg { width: 13px; height: 13px; fill: var(--green); flex: none; }
</style>
</head>
<body>
<main class="stage">

  <section class="card card--back" aria-label="Business card back">
    <div class="back__scene" role="img" aria-label="Green illustration of sunrise over mountains and vineyard rows"></div>
    <div class="back__band">
      <p class="back__tagline">An authentic and boutique wine tour experience</p>
    </div>
  </section>

  <section class="card card--front" aria-label="Business card front">
    <div class="front__brand">
      <span class="brand__mark"></span>
      <span class="brand__name">Cork Hollow Excursions</span>
    </div>
    <h1 class="front__name">Dale Munford</h1>
    <div class="front__rule"></div>
    <ul class="front__contacts">
      <li class="contact">805-291-6384
        <svg viewBox="0 0 24 24" aria-hidden="true"><path d="M6.6 10.8a15.1 15.1 0 0 0 6.6 6.6l2.2-2.2a1 1 0 0 1 1-.25 11.4 11.4 0 0 0 3.6.57 1 1 0 0 1 1 1V20a1 1 0 0 1-1 1A17 17 0 0 1 3 4a1 1 0 0 1 1-1h3.5a1 1 0 0 1 1 1c0 1.25.2 2.45.57 3.57a1 1 0 0 1-.25 1z"/></svg>
      </li>
      <li class="contact">info@corkhollowexcursions.com
        <svg viewBox="0 0 24 24" aria-hidden="true"><path d="M2 5h20v14H2z M2 5l10 8 10-8" fill="none" stroke="#23633f" stroke-width="2.2"/></svg>
      </li>
      <li class="contact">corkhollowexcursions.com
        <svg viewBox="0 0 24 24" aria-hidden="true"><circle cx="12" cy="12" r="10"/><path d="M2 12h20M12 2c3 3 3 17 0 20M12 2c-3 3-3 17 0 20" fill="none" stroke="#ffffff" stroke-width="1.5"/></svg>
      </li>
    </ul>
  </section>

</main>
</body>
</html>
```